SEO AND WEB DESIGN COMPANY BUSINESS CARD DESIGN

I need an eye catching , simple business card design that will match my logo . I need 2 versions of it ( white background and black background) - SOME PEOPLE DID NOT GET IT AND SENDING US FRONT WHITE BACK WHITE VERSIONS WHICH IS NOT CORRECT.

ONE VERSION SHOULD BE BACK AND FRONT ALL BLACK , SECOND VERSION SHOULD BE BACK AND FRONT ALL WHITE

logo psd files are attached for both versions. The business card is going to have : First Name- Last name - position - phone numbers

```html
<!DOCTYPE html>
<html lang="en">
<head>
<meta charset="utf-8">
<title>Vertex Studio Business Cards</title>
<link rel="stylesheet" href="https://fonts.googleapis.com/css2?family=Oswald:wght@500&family=Source+Sans+3:wght@400;700&display=swap">
<style>
  :root {
    --backdrop: #2a2a2a;
    --card-white: #ffffff;
    --card-black: #000000;
    --ink: #1a1a1a;
    --ink-soft: #3c3c3c;
    --accent: #3a96ee;
    --rule: #a8a8a8;
  }
  * { margin: 0; padding: 0; box-sizing: border-box; }
  html, body { width: 1200px; height: 960px; overflow: hidden; }
  body {
    background: var(--backdrop);
    position: relative;
    font-family: "Source Sans 3", "Myriad Pro", sans-serif;
  }
  .card {
    position: absolute;
    left: 262px;
    width: 678px;
    box-shadow: 0 6px 18px rgba(0,0,0,.55);
  }
  .card--front { top: 61px; height: 388px; background: var(--card-white); }
  .card--back { top: 512px; height: 385px; background: var(--card-black); }

  .brand {
    position: absolute;
    right: 43px;
    top: 118px;
    display: flex;
    align-items: center;
    gap: 10px;
    font-family: "Oswald", sans-serif;
    font-weight: 500;
    font-size: 44px;
    line-height: 1;
    color: var(--ink);
    letter-spacing: 0.5px;
  }
  .brand__dot { width: 16px; height: 16px; border-radius: 50%; background: var(--accent); }

  .person { position: absolute; left: 41px; top: 186px; }
  .person__name { font-weight: 700; font-size: 23px; color: var(--accent); line-height: 1.1; }
  .person__role { font-size: 17px; color: var(--ink); margin-top: 2px; }

  .divider {
    position: absolute; left: 41px; top: 244px;
    width: 586px; height: 2px; background: var(--rule);
  }

  .contacts { position: absolute; left: 41px; top: 262px; list-style: none; }
  .contacts li {
    display: flex; align-items: center; gap: 12px;
    font-size: 17px; color: var(--ink-soft); height: 22px;
  }
  .contacts svg { width: 16px; height: 16px; fill: var(--accent); flex: none; }

  .address {
    position: absolute; right: 42px; top: 285px;
    text-align: right; font-size: 17px; line-height: 22px; color: var(--ink-soft);
  }

  .band-line { position: absolute; left: 0; right: 0; top: 368px; height: 3px; background: var(--ink); }
  .band { position: absolute; left: 0; right: 0; bottom: 0; height: 16px; background: var(--accent); }

  .back-brand {
    position: absolute; left: 0; right: 0; top: 140px;
    text-align: center;
    font-family: "Oswald", sans-serif; font-weight: 500;
    font-size: 86px; line-height: 1; color: var(--card-white);
  }
  .back-rule {
    position: absolute; left: 158px; width: 362px; top: 235px; height: 3px;
    background: linear-gradient(90deg, transparent, var(--accent) 20%, var(--accent) 80%, transparent);
  }
  .back-url {
    position: absolute; left: 0; right: 0; top: 333px;
    text-align: center; font-size: 17px; letter-spacing: 2.6px;
    color: var(--card-white);
  }
</style>
</head>
<body>
  <section class="card card--front" aria-label="Business card front">
    <div class="brand"><span class="brand__dot"></span>VERTEX STUDIO</div>

    <div class="person">
      <p class="person__name">Jordan Hale</p>
      <p class="person__role">President</p>
    </div>

    <div class="divider"></div>

    <ul class="contacts">
      <li><svg viewBox="0 0 16 16"><path d="M1 5c0-2 2-3 7-3s7 1 7 3v1h-4V4.5H5V6H1zM3 7h10l2 7H1zm5 1.5a2.5 2.5 0 1 0 0 5 2.5 2.5 0 0 0 0-5z"/></svg>(555) 0142-7781</li>
      <li><svg viewBox="0 0 16 16"><path d="M4 0h8a1 1 0 0 1 1 1v14a1 1 0 0 1-1 1H4a1 1 0 0 1-1-1V1a1 1 0 0 1 1-1zm1 2v10h6V2zm3 11a1 1 0 1 0 0 2 1 1 0 0 0 0-2z"/></svg>(555) 0198-3364</li>
      <li><svg viewBox="0 0 16 16"><path d="M4 1h8v4H4zM1 6h14v6h-3v3H4v-3H1zm4 4v4h6v-4z"/></svg>(555) 0167-2290</li>
      <li><svg viewBox="0 0 16 16"><path d="M1 3h14v1.5L8 9 1 4.5zm0 3.3 7 4.5 7-4.5V13H1z"/></svg>hello@vertexstudio.com</li>
    </ul>

    <div class="address">
      <p>2417 Larkspur Lane</p>
      <p>Cedar Grove, NY 11020</p>
      <p>www.vertexstudio.com</p>
    </div>

    <div class="band-line"></div>
    <div class="band"></div>
  </section>

  <section class="card card--back" aria-label="Business card back">
    <p class="back-brand">VERTEX STUDIO</p>
    <div class="back-rule"></div>
    <p class="back-url">www.vertexstudiodesign.com</p>
  </section>
</body>
</html>
```